Kestonvale Hawks FC Website

We are looking to develop a new website for Kestonvale FC. Kestonvale FC has now joined with Kestonvale Hawks FC and we are looking at a website that can work for both clubs. Kestonvale FC play in a local park football competition while kestonvale Hawks are a Semi Professional team that plays in the Harbourline Premier Division Competition. What we are after is two separate website off the one platform. I have attached both team logos for you to visualise. Also you can look at the existing kestonvale website www.kestonvalefc.com.au. We are looking for a huge improvement in the website and it will be imperative we have links to sponsors and the sponsors can get regular visuals. Weare looking to move this club forward and have a very professional website that can communicate clearly with the community.

Hi All,

Please remember that the website is to represent two clubs;
1. Kestonvale Hawks FC (Competes in Semi Professional League)
2. Kestonvale FC (Compete in TMCJA League which is a lower level)

Further to this the Kestonvale Hawks FC page will require a player profile page which will show photos of each player and a little bio on each.

Thanks

Reason: Would like to spend more time review existing and new designs

```html
<!DOCTYPE html>
<html lang="en">
<head>
<meta charset="utf-8">
<title>Kestonvale FC</title>
<link rel="stylesheet" href="https://fonts.googleapis.com/css2?family=Open+Sans:ital,wght@0,300;0,400;0,600;1,400&display=swap">
<style>
:root{
  --red:#d0021b;
  --ink:#333333;
  --ink-soft:#444a4f;
  --muted:#8a8a8a;
  --rule:#dcdcdc;
  --nav-bg:#f3f3f1;
  --hero-dark:#1e1e1c;
  --white:#ffffff;
  --panel:#d3d3d3;
}
*{margin:0;padding:0;box-sizing:border-box}
html,body{width:1200px;height:900px;overflow:hidden;background:var(--white);font-family:"Open Sans",Arial,sans-serif;color:var(--ink)}
.page{position:relative;width:1200px;height:900px;overflow:hidden}
.top-rule{position:absolute;left:0;top:0;width:1200px;height:4px;background:var(--red)}

.club-mark{position:absolute;left:129px;top:22px;width:130px;height:134px;display:flex;flex-direction:column;align-items:center;justify-content:center;gap:10px}
.club-mark .dot{width:54px;height:54px;border-radius:50%;border:3px solid var(--red)}
.club-mark .mark-name{font-size:13px;font-weight:600;color:var(--red);letter-spacing:.5px;text-transform:uppercase}

.site-title{position:absolute;left:313px;top:40px;font-size:38px;font-weight:400;letter-spacing:.5px;color:var(--red);line-height:1}
.site-title .suffix{color:var(--ink-soft);font-weight:600}

.main-nav{position:absolute;left:265px;top:114px;width:935px;height:37px;background:linear-gradient(90deg,rgba(243,243,241,0),var(--nav-bg) 40px);border-top:1px solid var(--rule);border-bottom:1px solid var(--rule)}
.main-nav ul{list-style:none;display:flex;position:absolute;left:35px;top:0;height:36px}
.main-nav li{font-size:15px;text-transform:uppercase;color:var(--ink);line-height:36px;margin-right:24px;position:relative}
.main-nav li.active{color:var(--red)}
.main-nav li.active::before{content:"";position:absolute;left:-2px;right:-2px;top:-1px;height:2px;background:var(--red)}
.main-nav li.active::after{content:"";position:absolute;left:50%;top:1px;margin-left:-4px;border:4px solid transparent;border-top-color:var(--red)}
.nav-divider{position:absolute;left:751px;top:8px;width:1px;height:20px;background:var(--rule)}
.search-icon{position:absolute;left:786px;top:9px}

.hero{position:absolute;left:0;top:175px;width:1200px;height:403px;border-top:4px solid var(--red);border-bottom:5px solid var(--red);background:var(--hero-dark);overflow:hidden}
.hero-photo{position:absolute;inset:0;background:
  radial-gradient(ellipse 320px 260px at 380px 300px,rgba(190,170,140,.75),rgba(80,70,60,.4) 60%,transparent 80%),
  radial-gradient(ellipse 200px 260px at 340px 160px,rgba(170,40,40,.55),transparent 70%),
  linear-gradient(90deg,#2a2826 0%,#5a554e 35%,#3a3834 60%,#1e1e1c 80%)}
.hero-copy{position:absolute;left:639px;top:80px;color:var(--white)}
.hero-copy h1{font-size:46px;font-weight:400;line-height:1.1}
.hero-copy .date{font-size:22px;font-style:italic;line-height:26px;margin-top:14px}
.hero-copy p{font-size:14px;line-height:22px;margin-top:14px}
.btn-outline{display:inline-block;margin-top:24px;margin-left:-1px;width:140px;height:37px;border:1px solid var(--white);text-align:center;line-height:35px;font-size:15px;font-weight:600;text-transform:uppercase;color:var(--white)}
.slider-dots{position:absolute;left:959px;top:358px;display:flex;gap:8px}
.slider-dots span{width:11px;height:11px;border-radius:50%;background:#5e5c57}
.slider-dots span.on{background:var(--red)}

.section-head{position:absolute;top:614px;border-bottom:1px solid var(--rule);height:53px}
.section-head h2{font-size:37px;font-weight:400;line-height:44px;text-transform:uppercase;color:var(--ink)}
.section-head::after{content:"";position:absolute;left:0;bottom:-1px;width:60px;height:2px;background:var(--red)}
.news-head{left:129px;width:560px}
.news-head .archive{position:absolute;right:0;top:30px;font-size:13px;color:var(--muted)}
.reg-head{left:769px;width:300px}

.news-title{position:absolute;left:129px;top:698px;font-size:26px;font-weight:400;color:var(--ink)}
.news-photo-frame{position:absolute;left:129px;top:746px;width:560px;height:170px;border:1px solid var(--rule);padding:5px}
.news-photo{width:100%;height:100%;background:linear-gradient(135deg,#1c1c1c 0%,#2a2a2a 30%,#c8131f 45%,#d91a22 100%)}

.register-card{position:absolute;left:769px;top:716px;width:301px;height:200px;background:linear-gradient(90deg,#d0d0d0,#dadada)}
.register-card .line1{position:absolute;left:23px;top:14px;font-size:47px;font-weight:300;color:var(--ink);line-height:1}
.register-card .line2{position:absolute;left:23px;top:62px;font-size:55px;font-weight:400;color:var(--red);line-height:1}
.register-card .season{position:absolute;left:23px;top:126px;font-size:18px;font-weight:600;color:var(--ink)}
.register-card .cta-band{position:absolute;left:0;top:164px;width:100%;height:40px;background:#2b2b2b}
.register-card .cta-band span{position:absolute;left:23px;top:4px;font-size:20px;font-weight:600;color:var(--red);text-transform:uppercase}
</style>
</head>
<body>
<div class="page">
  <div class="top-rule"></div>

  <header>
    <div class="club-mark">
      <span class="dot"></span>
      <span class="mark-name">Kestonvale FC</span>
    </div>
    <div class="site-title">KESTONVALE <span class="suffix">FC</span></div>
    <nav class="main-nav">
      <ul>
        <li>Home</li>
        <li>News</li>
        <li>Fixture &amp; Results</li>
        <li>Photo Gallery</li>
        <li class="active">Sponsor Club</li>
        <li>Contact Us</li>
      </ul>
      <span class="nav-divider"></span>
      <svg class="search-icon" width="18" height="18" viewBox="0 0 18 18" aria-label="Search">
        <circle cx="7" cy="7" r="5" fill="none" stroke="#333" stroke-width="2.2"/>
        <line x1="10.8" y1="10.8" x2="16" y2="16" stroke="#333" stroke-width="2.8" stroke-linecap="round"/>
      </svg>
    </nav>
  </header>

  <section class="hero">
    <div class="hero-photo" role="img" aria-label="Footballer in a red kit leaping to strike a smoking ball against a dark, misty stadium background"></div>
    <div class="hero-copy">
      <h1>TMCJA Charity Day</h1>
      <div class="date">Charity Day Sunday 16th march 2014,<br>11Am Kick Off</div>
      <p>Come and enjoy a fun family day whilst supporting<br>The Riverbend Children's Hospital</p>
      <a class="btn-outline">Learn More</a>
    </div>
    <div class="slider-dots"><span class="on"></span><span></span><span></span><span></span><span></span><span></span></div>
  </section>

  <div class="section-head news-head"><h2>Latest News</h2><span class="archive">Archive</span></div>
  <div class="section-head reg-head"><h2>Registration</h2></div>

  <h3 class="news-title">Information night</h3>
  <div class="news-photo-frame">
    <div class="news-photo" role="img" aria-label="Close-up of a silver medal resting on a red club shirt"></div>
  </div>

  <div class="register-card">
    <div class="line1">REGISTER</div>
    <div class="line2">ONLINE</div>
    <div class="season">2014 SEASON</div>
    <div class="cta-band"><span>Click Here</span></div>
  </div>
</div>
</body>
</html>
```